Chilled (açaí bowls)

I’m starting a Portable açaí bowl business for TV and movie sets, I have a little ice cream cart with an umbrella, and I’m a petite Brown haired young woman. I’d like to either put a silhouette of myself into the card or just the ice cream cart or something more creative, I have no idea what it should look like yet

Target Market(s)

Entertainment industry craft service officials

Contact Information for Business Card

Would love it to be somewhat colorful

Colors

Designer to choose colors to be used in the design.

Requirements
Must have
• Nora Patchett
• Norabyday@fernmail.example
• 310-428-9073
• Chilled (Business name)
Nice to have
• Ice cream cart w/ umbrella

```html
<!DOCTYPE html>
<html lang="en">
<head>
<meta charset="utf-8">
<title>Chilled – Business Card</title>
<link rel="stylesheet" href="https://fonts.googleapis.com/css2?family=Montserrat:wght@400;600;800&display=swap">
<style>
  :root {
    --bg: #2b2d31;
    --pink: #d6548f;
    --pink-light: #e26fa3;
    --white: #ffffff;
    --grey: #8a8a8d;
  }
  * { margin: 0; padding: 0; box-sizing: border-box; }
  html, body { width: 1200px; height: 900px; overflow: hidden; }
  body {
    background: var(--bg);
    font-family: "Montserrat", sans-serif;
    display: flex;
    align-items: center;
    justify-content: center;
    gap: 48px;
  }
  .card {
    width: 518px;
    height: 296px;
    border-radius: 4px;
    box-shadow: 0 12px 30px rgba(0,0,0,.45);
    position: relative;
    overflow: hidden;
  }
  .card--front { background: var(--white); display: flex; align-items: center; }
  .card--back {
    background: linear-gradient(135deg, var(--pink) 0%, var(--pink-light) 55%, var(--pink) 100%);
    display: flex; align-items: center; justify-content: center;
  }
  .brand {
    width: 44%;
    display: flex;
    align-items: center;
    justify-content: center;
    gap: 10px;
  }
  .brand__dot { width: 14px; height: 14px; border-radius: 50%; background: var(--pink); }
  .brand__name {
    font-weight: 800;
    font-size: 38px;
    color: var(--pink);
    letter-spacing: 1px;
    text-transform: uppercase;
  }
  .card--back .brand { width: auto; }
  .card--back .brand__dot { background: var(--white); width: 18px; height: 18px; }
  .card--back .brand__name { color: var(--white); font-size: 56px; }
  .divider { width: 1.5px; height: 120px; background: var(--pink); }
  .contact { padding-left: 26px; }
  .contact__name {
    font-weight: 600;
    font-size: 17px;
    letter-spacing: 1.5px;
    color: var(--pink);
    text-transform: uppercase;
    margin-bottom: 14px;
  }
  .contact__row {
    display: flex;
    align-items: center;
    gap: 9px;
    font-size: 13px;
    color: var(--grey);
    line-height: 1.9;
  }
  .contact__row svg { width: 13px; height: 13px; fill: var(--pink); flex: none; }
  .contact__row strong { color: var(--pink); font-weight: 600; }
</style>
</head>
<body>
  <section class="card card--front">
    <div class="brand">
      <span class="brand__dot"></span>
      <span class="brand__name">Chilled</span>
    </div>
    <div class="divider"></div>
    <div class="contact">
      <p class="contact__name">Nora Patchett</p>
      <p class="contact__row">
        <svg viewBox="0 0 24 24"><path d="M6.6 10.8a15.1 15.1 0 0 0 6.6 6.6l2.2-2.2a1 1 0 0 1 1-.25 11.4 11.4 0 0 0 3.6.57 1 1 0 0 1 1 1V20a1 1 0 0 1-1 1A17 17 0 0 1 3 4a1 1 0 0 1 1-1h3.5a1 1 0 0 1 1 1c0 1.25.2 2.45.57 3.57a1 1 0 0 1-.25 1z"/></svg>
        310-428-9073
      </p>
      <p class="contact__row">
        <svg viewBox="0 0 24 24"><path d="M2 5h20v14H2z M3.5 6.5 12 13l8.5-6.5" fill="none" stroke="#d6548f" stroke-width="2"/></svg>
        Norabyday@fernmail.example
      </p>
      <p class="contact__row">
        <svg viewBox="0 0 24 24"><circle cx="12" cy="12" r="9" fill="none" stroke="#d6548f" stroke-width="2"/><path d="M3 12h18M12 3c3 3 3 15 0 18M12 3c-3 3-3 15 0 18" fill="none" stroke="#d6548f" stroke-width="1.6"/></svg>
        <span>www.<strong>chilled</strong>.example</span>
      </p>
    </div>
  </section>

  <section class="card card--back">
    <div class="brand">
      <span class="brand__dot"></span>
      <span class="brand__name">Chilled</span>
    </div>
  </section>
</body>
</html>
```